This is a laser engraving business. I’m looking for a business card that includes a minimalist laser logo/design with the company name Brisk Harbor Crafts and telephone number 654-210-3378 and email briskharborcrafts@mailrove.com

Industry/Entity Type

Laser engraving

Contact Information for Business Card

Laser logo/design that represents laser engraving

```html
<!DOCTYPE html>
<html lang="en">
<head>
<meta charset="utf-8">
<title>Brisk Harbor Crafts — Business Cards</title>
<link rel="stylesheet" href="https://fonts.googleapis.com/css2?family=Arimo:wght@700&display=swap">
<style>
  :root {
    --page-bg: #ffffff;
    --card-dark: #2c2d2c;
    --metal-deep: #8d857a;
    --metal-mid: #c4bcaf;
    --metal-light: #f2eee6;
    --tan: #e8b27a;
    --amber: #f2a43a;
    --navy: #27235f;
    --ornament-silver: #cfc8bb;
    --ornament-shadow: #2a2b2a;
  }
  * { box-sizing: border-box; margin: 0; padding: 0; }
  html, body {
    width: 1200px;
    height: 738px;
    overflow: hidden;
    background: var(--page-bg);
  }
  .canvas {
    position: relative;
    width: 1200px;
    height: 738px;
    display: flex;
    align-items: center;
    justify-content: center;
    gap: 20px;
  }
  .card {
    position: relative;
    width: 570px;
    height: 326px;
    overflow: hidden;
    font-family: "Arimo", Arial, sans-serif;
    font-weight: 700;
  }
  .card--dark { background: var(--card-dark); }
  .card--metal {
    background: linear-gradient(118deg,
      var(--metal-deep) 0%,
      var(--metal-mid) 30%,
      var(--metal-light) 48%,
      var(--metal-mid) 64%,
      var(--metal-deep) 100%);
  }
  .ornament {
    position: absolute;
    border-radius: 50%;
    background: radial-gradient(circle,
      var(--ornament-silver) 0%,
      #9c958a 35%,
      var(--ornament-shadow) 60%,
      #8e877c 78%,
      var(--ornament-silver) 92%);
    box-shadow: 0 0 10px rgba(0,0,0,0.35);
  }
  .ornament--large { width: 330px; height: 330px; left: 328px; top: -65px; }
  .ornament--small { width: 156px; height: 156px; left: -36px; top: 186px; }
  .brand {
    position: absolute;
    left: 26px;
    top: 48px;
    display: flex;
    align-items: center;
    gap: 10px;
  }
  .brand-mark {
    width: 16px;
    height: 16px;
    background: var(--tan);
  }
  .brand-name {
    font-size: 21px;
    letter-spacing: 1.2px;
    text-transform: uppercase;
    white-space: nowrap;
  }
  .card--dark .brand-name { color: var(--tan); }
  .card--metal .brand-name { color: var(--navy); }
  .contact {
    position: absolute;
    left: 154px;
    display: flex;
    align-items: center;
    gap: 8px;
    font-size: 17px;
    letter-spacing: 1px;
    white-space: nowrap;
  }
  .contact--phone { top: 218px; font-size: 19px; letter-spacing: 1.6px; }
  .contact--email { top: 271px; }
  .card--dark .contact { color: var(--amber); }
  .card--metal .contact { color: var(--navy); }
  .contact-icon { width: 14px; height: 14px; flex: none; }
  .card--dark .contact-icon { fill: var(--amber); }
  .card--metal .contact-icon { fill: var(--navy); }
</style>
</head>
<body>
<main class="canvas">

  <section class="card card--dark">
    <div class="ornament ornament--large" role="img" aria-label="Large silver lace mandala ornament"></div>
    <div class="ornament ornament--small" role="img" aria-label="Small silver lace mandala ornament"></div>
    <div class="brand">
      <span class="brand-mark"></span>
      <span class="brand-name">Brisk Harbor Crafts</span>
    </div>
    <p class="contact contact--phone">
      <svg class="contact-icon" viewBox="0 0 24 24" aria-hidden="true"><path d="M6.6 10.8a15.1 15.1 0 0 0 6.6 6.6l2.2-2.2a1 1 0 0 1 1-.25 11.4 11.4 0 0 0 3.6.57 1 1 0 0 1 1 1V20a1 1 0 0 1-1 1A17 17 0 0 1 3 4a1 1 0 0 1 1-1h3.5a1 1 0 0 1 1 1c0 1.25.2 2.45.57 3.57a1 1 0 0 1-.25 1z"/></svg>
      654-210-3378
    </p>
    <p class="contact contact--email">
      <svg class="contact-icon" viewBox="0 0 24 24" aria-hidden="true"><path d="M2 5h20v14H2z M2 5l10 8 10-8" /><path d="M3 6l9 7 9-7" fill="#2c2d2c"/></svg>
      briskharborcrafts@mailrove.com
    </p>
  </section>

  <section class="card card--metal">
    <div class="ornament ornament--large" role="img" aria-label="Large dark and silver lace mandala ornament"></div>
    <div class="ornament ornament--small" role="img" aria-label="Small dark and silver lace mandala ornament"></div>
    <div class="brand">
      <span class="brand-mark"></span>
      <span class="brand-name">Brisk Harbor Crafts</span>
    </div>
    <p class="contact contact--phone">
      <svg class="contact-icon" viewBox="0 0 24 24" aria-hidden="true"><path d="M6.6 10.8a15.1 15.1 0 0 0 6.6 6.6l2.2-2.2a1 1 0 0 1 1-.25 11.4 11.4 0 0 0 3.6.57 1 1 0 0 1 1 1V20a1 1 0 0 1-1 1A17 17 0 0 1 3 4a1 1 0 0 1 1-1h3.5a1 1 0 0 1 1 1c0 1.25.2 2.45.57 3.57a1 1 0 0 1-.25 1z"/></svg>
      654-210-3378
    </p>
    <p class="contact contact--email">
      <svg class="contact-icon" viewBox="0 0 24 24" aria-hidden="true"><path d="M2 5h20v14H2z"/><path d="M3 6l9 7 9-7" fill="#d8d2c6"/></svg>
      briskharborcrafts@mailrove.com
    </p>
  </section>

</main>
</body>
</html>
```